4 'Thank you' greetings cards designs

We are a small greetings card publisher and we need designs for a range of 'Thank you' greetings cards and notecards.
This project is for a total of 4 designs.
Please take a look at this board on Moodpinly, to see the kind of thing we are looking for: https://www.moodpinly.example/dorvek481/thank-you-cards/
The cards will be printed at a maximum size of 131mm x 183mm (including a 3mm bleed) so please provide 300dpi CMYK files at this size. Please ensure that any text (or elements of the design that are not part of the bleed) are at least 11mm in from each edge. Also, please note that cards do not have to have a bleed if your design doesn't require it (e.g. a plain white background).
Please provide 2 designs in 'portrait' orientation and 2 in 'landscape'.
Please provide 2 designs that just have the words 'Thank you' and then 2 designs that include your choice of these alternative messages:
Thank you so much
Thanks very much
Thank you very much
Thanks a million
Just to say thank you
A big thank you
A really big thank you
Feel free to use an exclamation mark on a couple of your designs, if you wish!
Other than the above guidelines, everything else is up to you in terms of colours, fonts, shapes, etc. - but please use the Moodpinly board to see the kind of designs we are looking for.
Thank you!

```html
<!DOCTYPE html>
<html lang="en">
<head>
<meta charset="utf-8">
<title>Thanks a million! – greetings card</title>
<link rel="stylesheet" href="https://fonts.googleapis.com/css2?family=Bodoni+Moda:opsz,wght@6..96,400&display=swap">
<style>
  :root {
    --card-white: #ffffff;
    --rose-red: #e0383a;
    --rose-pink: #f6c9c9;
    --rose-blush: #fbe3e3;
    --leaf-green: #cfe6d6;
    --leaf-mint: #e6f2ea;
  }
  html, body {
    margin: 0;
    padding: 0;
    width: 1200px;
    height: 926px;
    overflow: hidden;
    background: var(--card-white);
  }
  .card {
    position: relative;
    width: 1200px;
    height: 926px;
    overflow: hidden;
    background: var(--card-white);
  }
  .rose-pattern {
    position: absolute;
    inset: 0;
    background:
      radial-gradient(circle at 8% 20%, var(--rose-pink) 0, transparent 9%),
      radial-gradient(circle at 32% 18%, var(--rose-pink) 0, transparent 9%),
      radial-gradient(circle at 52% 10%, var(--rose-pink) 0, transparent 8%),
      radial-gradient(circle at 50% 33%, var(--rose-pink) 0, transparent 9%),
      radial-gradient(circle at 76% 34%, var(--rose-pink) 0, transparent 9%),
      radial-gradient(circle at 92% 28%, var(--rose-pink) 0, transparent 8%),
      radial-gradient(circle at 36% 68%, var(--rose-pink) 0, transparent 9%),
      radial-gradient(circle at 60% 78%, var(--rose-pink) 0, transparent 8%),
      radial-gradient(circle at 87% 79%, var(--rose-pink) 0, transparent 8%),
      radial-gradient(circle at 8% 90%, var(--rose-pink) 0, transparent 8%),
      radial-gradient(circle at 11% 25%, var(--leaf-green) 0, transparent 11%),
      radial-gradient(circle at 66% 40%, var(--leaf-green) 0, transparent 10%),
      radial-gradient(circle at 39% 75%, var(--leaf-green) 0, transparent 10%),
      radial-gradient(circle at 88% 85%, var(--leaf-green) 0, transparent 10%),
      radial-gradient(ellipse at 30% 40%, var(--rose-blush) 0%, transparent 60%),
      radial-gradient(ellipse at 70% 65%, var(--leaf-mint) 0%, transparent 60%),
      var(--card-white);
  }
  .greeting {
    position: absolute;
    left: 0;
    right: 0;
    top: 402px;
    margin: 0;
    text-align: center;
    font-family: "Bodoni Moda", serif;
    font-weight: 400;
    font-size: 104px;
    line-height: 1;
    letter-spacing: -1px;
    color: var(--rose-red);
  }
</style>
</head>
<body>
  <main class="card">
    <div class="rose-pattern" role="img" aria-label="Scattered hand-drawn red roses with green stems and leaves, in large and small sizes, covering a white background"></div>
    <h1 class="greeting">Thanks a million!</h1>
  </main>
</body>
</html>
```